Create the design of Sitepelican (in photoshop or similar)

*edit* What we wanna see is a sketch of a first page, and then in the end 5 page designs, but the main page will be the big tasks other pages are just basically pop-ups or form. *edit*

We need a web design for our new startup Sitepelican in turn will be providing web pages to smaller business. So the purpose of the page is to clearly showcase the message in a web 3.0 fashion, good design looks but function should always be the main focus.Further more we are looking for a long term relationship with a good designer / design company that can help us design the future web sites for our customers as well.

We need you to understand web, not just design. You need to be up to date with how web looks and works, and how to make it as simple and easy to use as possible for the customer and at the same time good looking.

Please look at the PDF for full description of the project.

Colors and layout are free to choose, but we really like the kind of layout that forkglider.com has so feel free to be inspired by them.

We want all of the pages design, but the main/landing page will be the big part, the rest are small pages that will use the same design frame as the main page.

PS. We just want the design in photoshop or illustrator format, the website will then be built in page tidal by page tidal experts (let us know if you/company also possess this knowledge)

Target Market(s)

Small to medium sized business, mostly owner/entrepreneur driven companies.

Industry/Entity Type

Business

Font styles to use
Other font styles liked:
• Helvetica for the win

Requirements
Must have
• Great and simple design, a child should be able to understand the message and also enjoy reading it. Should be a funny website while still being professional, i.e. see postbadger.com for example.

```html
<!DOCTYPE html>
<html lang="en">
<head>
<meta charset="utf-8">
<title>Sitepelican</title>
<link href="https://fonts.googleapis.com/css2?family=Aldrich&family=Ubuntu:wght@400;500&family=Arimo:wght@400;700&display=swap" rel="stylesheet">
<style>
:root{
  --dark:#333333;
  --cyan:#17b8e0;
  --text:#6e6e6e;
  --heading:#333;
  --line:#e2e2e2;
  --field:#eeeeee;
  --orange:#d9512c;
  --link:#2a6fb3;
}
*{margin:0;padding:0;box-sizing:border-box}
html,body{width:1200px;height:1163px;overflow:hidden;background:#fff}
body{position:relative;font-family:"Ubuntu",sans-serif;color:var(--text)}
.abs{position:absolute}

.site-header{position:absolute;left:0;top:0;width:1200px;height:70px;background:var(--dark)}
.brand{position:absolute;left:86px;top:9px;font-family:"Ubuntu",sans-serif}
.brand-name{font-size:34px;line-height:34px;font-weight:500;color:var(--cyan);letter-spacing:1px}
.brand-tag{font-size:11.5px;color:#fff;margin-top:3px}
.main-nav{position:absolute;left:408px;top:0;display:flex;height:70px;font-family:"Ubuntu",sans-serif;font-size:13.5px;color:#fff;white-space:nowrap}
.main-nav a{display:flex;align-items:center;padding:0 21px;color:#fff;text-decoration:none;height:70px;white-space:nowrap}
.main-nav a.active{background:var(--cyan)}

.feature{position:absolute;top:124px;width:348px;height:339px;border:1px solid var(--line)}
.feature-icon{position:absolute;left:128px;top:20px;width:90px;height:90px;border-radius:50%;border:4px solid #f0f0f0}
.feature-icon.cyan{background:var(--cyan)}
.feature-icon.grey{background:#999}
.feature h2{position:absolute;top:127px;left:0;width:100%;text-align:center;font-family:"Aldrich",sans-serif;font-weight:400;font-size:18px;color:var(--heading);white-space:nowrap}
.feature p,.feature li{font-size:12px;line-height:16px;color:var(--text)}
.feature ul{position:absolute;left:16px;top:158px;list-style:none;width:310px}
.feature li{padding-left:16px;position:relative;margin-bottom:13px}
.feature li::before{content:"★";position:absolute;left:0;top:0;color:#777}
.btn{position:absolute;background:var(--cyan);color:#fff;font-size:12px;display:flex;align-items:center;justify-content:center;text-transform:uppercase}

.calc-title{position:absolute;left:70px;top:482px;font-size:25px;color:#333;white-space:nowrap}
.calc-label{position:absolute;top:530px;font-family:"Arimo",sans-serif;font-size:19px;color:#666;white-space:nowrap}
.calc-field{position:absolute;top:560px;width:145px;height:34px;background:var(--field);border:1px solid #999;border-radius:3px;font-family:"Arimo",sans-serif;font-weight:700;font-size:18px;color:#222;padding:7px 8px}
.calc-field svg{position:absolute;right:9px;top:11px}
.calc-button{position:absolute;left:61px;top:613px;width:1077px;height:49px;background:var(--cyan);border-radius:4px;color:#fff;font-family:"Arimo",sans-serif;font-weight:700;font-size:37px;text-align:center;line-height:49px}

.col-title{position:absolute;top:688px;font-size:20px;font-weight:400;color:#333;letter-spacing:1px;white-space:nowrap}
.welcome{position:absolute;left:77px;top:727px;width:312px;font-size:12.3px;color:var(--text)}
.welcome p{line-height:22.4px;margin-bottom:10px}
.welcome p.alt{font-family:"Arimo",sans-serif;line-height:21.5px;font-size:12.5px}
.services{position:absolute;left:443px;top:720px;width:313px;list-style:none;font-family:"Arimo",sans-serif;font-size:12.7px;color:#777}
.services li{height:33.1px;line-height:34px;border-bottom:1px dashed #e0e0e0;padding-left:13px;position:relative;white-space:nowrap}
.services li::before{content:"›";position:absolute;left:0;top:-1px;font-size:15px;color:#444}

.chat{position:absolute;left:812px;top:720px;width:268px;height:368px;border:1px solid var(--line);font-family:"Arimo",sans-serif}
.chat-head{height:30px;background:var(--orange);color:#fff;font-size:13px;padding:8px 9px;border-radius:3px 3px 0 0}
.chat-msg{padding:8px 10px;font-size:11.8px;line-height:18.8px;color:#111}
.chat-msg span{color:var(--link)}
.chat-input{margin:0 10px 4px;height:27px;border:1px solid #ddd;font-size:11.5px;color:#999;padding:6px 4px;white-space:nowrap;overflow:hidden}
.chat-input.area{height:92px}
.chat-send{position:absolute;right:19px;top:317px;width:48px;height:24px;background:var(--cyan);color:#fff;border-radius:2px;font-size:13px;text-align:center;line-height:24px}
.chat-foot{position:absolute;left:0;bottom:2px;width:100%;text-align:center;font-size:7.5px;letter-spacing:1.5px;color:#999}
.chat-foot b{color:var(--orange)}

.site-footer{position:absolute;left:0;top:1112px;width:1200px;height:51px;background:var(--dark);font-size:12.3px}
.site-footer .copy{position:absolute;left:60px;top:18px;color:#bbb}
.site-footer .policy{position:absolute;right:22px;top:18px;color:var(--cyan)}
</style>
</head>
<body>

<header class="site-header">
  <div class="brand">
    <div class="brand-name">LOGO</div>
    <div class="brand-tag">most convenient web ever</div>
  </div>
  <nav class="main-nav">
    <a class="active">Home</a><a>About Us</a><a>How it works</a><a>FAQ</a><a>What people think?</a><a>Order</a><a>Contact Us</a>
  </nav>
</header>

<section class="feature" style="left:60px">
  <div class="feature-icon cyan" role="img" aria-label="Rocket with question mark icon"></div>
  <h2>WHAT IS SITEPELICAN?</h2>
  <ul>
    <li>Your website on subscription autopilot with free unlimited support and updates.</li>
    <li>Delivered by professionals.</li>
  </ul>
  <div class="btn" style="left:114px;top:246px;width:121px;height:36px">Read more</div>
</section>

<section class="feature" style="left:425px">
  <div class="feature-icon grey" role="img" aria-label="Money bag icon"></div>
  <h2>WHAT DOES IT COST?</h2>
  <p class="abs" style="left:17px;top:164px;width:320px">About the same as a day and guaranteed less than a really good night out with&nbsp; the gang.</p>
  <p class="abs" style="left:18px;top:206px">See price details</p>
  <div class="btn" style="left:113px;top:237px;width:121px;height:36px">Read more</div>
</section>

<section class="feature" style="left:790px">
  <div class="feature-icon grey" role="img" aria-label="Unhappy icon"></div>
  <h2>IF YOU ARE UNHAPPY?</h2>
  <p class="abs" style="left:16px;top:164px;width:325px;line-height:21.5px">Cancel the same day, we will refund you all your money and buy you a year of Tunebarrel subscription</p>
</section>

<h2 class="calc-title" style="font-weight:400">Test your website now! How many more customers could you get every month?</h2>
<div class="calc-label" style="left:81px">Visitors per month</div>
<div class="calc-label" style="left:311px">Current conversion rate in</div>
<div class="calc-label" style="left:610px">Improve conversion rate</div>
<div class="calc-label" style="left:899px">Average purchase in SEK</div>
<div class="calc-field" style="left:85px">10,000</div>
<div class="calc-field" style="left:343px">1-5%</div>
<div class="calc-field" style="left:642px">1-3%</div>
<div class="calc-field" style="left:927px">SEK
  <svg width="16" height="14" viewBox="0 0 16 14"><path d="M0 0H16L8 14Z" fill="#17b8e0"/></svg>
</div>
<div class="calc-button">Calculate</div>

<h3 class="col-title" style="left:77px">WELCOME</h3>
<h3 class="col-title" style="left:443px">WHAT WE DO</h3>
<h3 class="col-title" style="left:810px">CHATWREN CHAT</h3>

<div class="welcome">
  <p>Lorem ipsum dolor sit amet, consectetur adipisicing elit, sed do eiusmod tempor incididunt ut labore et dolore magna aliqua. Ut enim ad minim veniam, quis nostrud exercitation ullamco laboris nisi ut aliquip ex ea commodo consequat. Duis aute irure dolor in reprehenderit in voluptate velit esse cillum dolore eu fugiat nulla pariatur.</p>
  <p class="alt">Lorem ipsum dolor sit amet, consectetur adipisicing elit, sed do eiusmod tempor incididunt ut labore et dolore magna aliqua. Ut enim ad minim veniam, quis nostrud exercitation ullamco laboris nisi ut aliquip ex ea commodo consequat. Duis aute irure dolor in reprehenderit in voluptate velit esse cillum dolore eu fugiat nulla pariatur.</p>
</div>
<div class="btn" style="left:76px;top:1060px;width:121px;height:36px">Read more</div>

<ul class="services">
  <li>Lorem ipsum dolor sit amet qui officia</li>
  <li>Duis aute irure dolor in culpa qui</li>
  <li>Sunt in culpa qui officia vel illum qui</li>
  <li>vel illum qui dolorem eum wise man therefore</li>
  <li>The wise man therefore in culpa qui officia</li>
  <li>Sunt in culpa qui officia culpa qui officia</li>
  <li>Lorem ipsum dolor sit amet qui officia</li>
  <li>Duis aute irure dolor in culpa qui</li>
  <li>Sunt in culpa qui officia vel illum qui</li>
  <li>vel illum qui dolorem eum wise man therefore</li>
</ul>

<aside class="chat">
  <div class="chat-head">After Hours Help</div>
  <div class="chat-msg">We're offline at the moment. You can search our <span>Help Center</span> for answers to many common getting started questions, or send us an email at support@chatwren.com if you don't find your answer right away. We'll back on live chat first thing Monday.</div>
  <div class="chat-input">Name (what should we call you?)</div>
  <div class="chat-input">Email (how do we reach you?)</div>
  <div class="chat-input area">Have a question about Chatwren live chat?</div>
  <div class="chat-send">Send</div>
  <div class="chat-foot">POWERED BY <b>CHATWREN</b></div>
</aside>

<footer class="site-footer">
  <span class="copy">Company Name © All Rights Reseverd</span>
  <span class="policy">Privacy Policy</span>
</footer>

</body>
</html>
```